Walkthrough Splash Page for new Content Management Site

Tallyroom.hive is a new site that helps groups and individuals design a custom site, create content and manage their members.

Although we have already designed a solid "root" homepage (see attached), we would like a set of default pages for when a person creates a new site that will help guide them through customizing their Space and creating content.

The "Root" Homepage is found here:
https://www.tallyroom.hive

An example of the current "default space" (which is what we need designed) can be found here:
https://freshroom.tallyroom.hive/

About the Functionality
This is some of the functionality that we would like covered in the design:
- A Tallyroom.hive Space is composed of two components: the "Space" and the "Dashboard".
- The Dashboard is used to (1) create content (e.g. Events, Auctions, Articles, Newsletters, etc.), (2) design the Space (by creating Pages, customizing the Menu and modifying overall styles), (3) view analytics about the space (e.g. how many members have viewed the space or have purchased a ticket, and (4) change their profile.
- User's can also use their profile to login/register for any other Tallyroom.hive Space as well.
- In the Dashboard you will see a "Profile" section and an "Account" section. The "Account" section is the User's relationship with the current Space. The "Profile" section will be follow the user around to any space that they are logged into.
- As you will see in the Dashboard, alot of the functionality has not yet been implemented, but please create the default page as if it has already been completed (it is coming soon).

Required Pages
We need four pages designed for the default new space: homepage, membership, about and contact.

The most important page is the default homepage which will help provide an example of what the user's Space can look and provide instructions on how to use the site (with links to the places on the site where these things can take place).

The default site also has a default "Membership", page which is a good change to demo another design to entire new people to sign up for the new Space as well as a "About" and "Contact" page.

We encourage you to visit our site (https://www.tallyroom.hive) to get a feel for our current design, which is based on Twitter Bootstrap and Vela Panel (http://skinvault.example/preview/QX7720391). To see a site that has already been created and customized, see the Harlow Ridge College Graduates Circle of New York (https://www.harlow-ridge.circle)

If you create a new Space you will see what the default page looks like (see attached).

I have also attached the Fonts, Icons and Color Palette that we currently use in the application - these are just to get you started, feel free to be creative!

Target Market(s)

Small groups, businesses and individuals who want to have an easy to way to create an online presence, especially those who wish to sell items online.

Industry/Entity Type

Management

Coding

Coded - Design and coding required

Number of Pages Required

4 page

Font styles to use
Serif
Other font styles liked:
• Movena Sans (Attached)

Colors
3276b5
33a6d7

Requirements
Must have
• Clean, tactile, responsive UI with pictures and diagrams.
• The site site takes on a high-tech, social approach to content management, which should be reflected in the design.

```html
<!DOCTYPE html>
<html lang="en">
<head>
<meta charset="utf-8">
<title>Tallyroom.hive</title>
<link href="https://fonts.googleapis.com/css2?family=Fira+Sans:wght@400;500;600&family=Oswald:wght@400&display=swap" rel="stylesheet">
<style>
:root{
  --blue:#3276b5;
  --blue-bright:#33a6d7;
  --blue-deep:#2c69a3;
  --hex-blue:#2f7bc0;
  --hex-blue-ring:#4a90cf;
  --hex-grey:#cfcfcf;
  --hex-grey-ring:#e4e4e4;
  --ink:#222;
  --body:#444;
  --panel:#f3f3f3;
  --white:#fff;
  --footer:#2b2b2b;
}
*{margin:0;padding:0;box-sizing:border-box}
html,body{width:786px;height:1200px;overflow:hidden}
body{position:relative;font-family:"Fira Sans",sans-serif;color:var(--body);background:var(--white)}
.topbar{position:absolute;left:0;top:0;width:786px;height:20px;background:var(--blue)}
.account-menu{position:absolute;left:635px;top:0;width:86px;height:20px;background:var(--blue-deep);color:var(--white);font-size:7.5px;display:flex;align-items:center;gap:4px;padding-left:8px}
.account-menu .ring{width:10px;height:10px;border:1px solid var(--white);border-radius:50%}
.account-menu .caret{margin-left:5px;border:3px solid transparent;border-top-color:var(--white);margin-top:3px}
.header{position:absolute;left:0;top:20px;width:786px;height:46px;background:var(--white)}
.brand{position:absolute;left:68px;top:8px;display:flex;align-items:center;gap:8px}
.brand .mark{width:30px;height:30px;border-radius:50%;background:var(--blue)}
.brand .name{font-size:22px;font-weight:500;color:var(--ink)}
.nav{position:absolute;top:22px;left:0;font-size:8px;color:#333;letter-spacing:.3px}
.nav a{position:absolute;white-space:nowrap;color:inherit;text-decoration:none}
.nav a.active{color:var(--blue)}
.btn-space{position:absolute;left:634px;top:13px;width:87px;height:24px;background:#eee;font-size:8px;font-weight:600;color:var(--ink);display:flex;align-items:center;justify-content:center;gap:6px}
.hero{position:absolute;left:0;top:66px;width:786px;height:278px;background:linear-gradient(100deg,#6b4a2c 0%,#8c6a48 30%,#b7a89a 50%,#7d5a3c 75%,#5e4128 100%)}
.hero-title{position:absolute;left:0;top:195px;width:786px;text-align:center;font-family:"Oswald",sans-serif;font-size:17px;line-height:21px;color:var(--white)}
.hero-rule{position:absolute;height:1px;background:rgba(255,255,255,.55)}
.features-left{position:absolute;left:0;top:344px;width:388px;height:490px;background:var(--panel)}
.feature{position:absolute;display:flex;align-items:center}
.feature svg{width:84px;height:72px;flex:none}
.feature .copy{margin-left:16px;width:195px}
.feature h3{font-size:12px;font-weight:600;color:var(--hex-blue);margin-bottom:5px}
.feature.grey h3{color:var(--ink)}
.feature p{font-size:8.3px;line-height:10.5px}
.showcase{position:absolute;left:0;top:834px;width:786px;height:179px;background:linear-gradient(120deg,#2a66a3,#3c88c8 55%,#2c6aa8)}
.device{position:absolute;top:864px;height:156px;background:linear-gradient(180deg,#1d1d1d 0%,#2e2e2e 88%,#c9c9c9 88%,#e8e8e8 100%);border-radius:6px 6px 3px 3px}
.showcase-caption{position:absolute;top:1033px;width:280px;text-align:center}
.showcase-caption h2{font-size:17px;font-weight:400;color:var(--ink);margin-bottom:8px}
.showcase-caption h2 span{color:var(--blue)}
.showcase-caption p{font-size:8.5px;line-height:13.5px}
.beta{position:absolute;left:0;top:1118px;width:786px;height:48px;background:var(--blue-deep)}
.beta h2{position:absolute;left:95px;top:11px;font-size:20px;font-weight:400;color:var(--white)}
.btn-site{position:absolute;left:583px;top:13px;width:87px;height:24px;background:var(--white);font-size:8px;font-weight:600;color:var(--ink);display:flex;align-items:center;justify-content:center;gap:7px}
.footer{position:absolute;left:0;top:1166px;width:786px;height:34px;background:var(--footer);color:#ddd;font-size:8.3px;text-align:center;line-height:34px}
</style>
</head>
<body>
<svg width="0" height="0" style="position:absolute">
  <defs>
    <symbol id="hex-blue" viewBox="0 0 84 72">
      <polygon points="0,36 21,0 63,0 84,36 63,72 21,72" fill="var(--hex-blue-ring)"/>
      <polygon points="7,36 24.5,6 59.5,6 77,36 59.5,66 24.5,66" fill="var(--hex-blue)"/>
    </symbol>
    <symbol id="hex-grey" viewBox="0 0 84 72">
      <polygon points="0,36 21,0 63,0 84,36 63,72 21,72" fill="var(--hex-grey-ring)"/>
      <polygon points="7,36 24.5,6 59.5,6 77,36 59.5,66 24.5,66" fill="var(--hex-grey)"/>
    </symbol>
  </defs>
</svg>

<div class="topbar"><div class="account-menu"><span class="ring"></span>Lorem Ispum<span class="caret"></span></div></div>

<header class="header">
  <div class="brand"><span class="mark"></span><span class="name">Tallyroom.hive</span></div>
  <nav class="nav">
    <a class="active" style="left:358px">HOME</a>
    <a style="left:412px">ABOUT US</a>
    <a style="left:482px">MEMBERSHIP</a>
    <a style="left:566px">CONTACT US</a>
  </nav>
  <div class="btn-space"><span style="font-size:12px">+</span>CEATE SPACE</div>
</header>

<section class="hero" role="img" aria-label="Photo of a desk with a laptop, clipboard, plant and paper clips"></section>
<div class="hero-rule" style="left:268px;top:195px;width:342px"></div>
<h1 class="hero-title">Tallyroom.hive Helps Groups Or Individuals Design A Custom Site,<br>Create Content And Manage Their Members.</h1>
<div class="hero-rule" style="left:177px;top:242px;width:432px"></div>

<section class="features-left"></section>

<div class="feature" style="left:85px;top:376px">
  <svg><use href="#hex-blue"/><g fill="none" stroke="#fff" stroke-width="2.5"><circle cx="42" cy="36" r="12"/><path d="M31 32 Q42 38 53 31 M36 25 Q44 36 38 47"/></g></svg>
  <div class="copy"><h3>Spaces</h3><p>Create a customizable Space to manage Members and content.</p></div>
</div>
<div class="feature" style="left:85px;top:464px">
  <svg><use href="#hex-blue"/><g fill="none" stroke="#fff" stroke-width="2.5"><rect x="37" y="21" width="10" height="18" rx="5"/><path d="M32 33 Q32 45 42 45 Q52 45 52 33 M42 45 V51 M36 51 H48"/></g></svg>
  <div class="copy"><h3>Newsletters</h3><p>Manage contacts and newsletters to reach your Members.</p></div>
</div>
<div class="feature" style="left:85px;top:552px">
  <svg><use href="#hex-blue"/><g fill="none" stroke="#fff" stroke-width="2.5"><rect x="33" y="21" width="18" height="27" rx="2"/><path d="M37 29 H47 M37 34 H47 M37 39 H47 M29 44 Q29 50 35 50 H51"/></g></svg>
  <div class="copy"><h3>Invoices</h3><p>Request ad hoc payments for a product or service from anyone.</p></div>
</div>
<div class="feature" style="left:85px;top:640px">
  <svg><use href="#hex-blue"/><g fill="none" stroke="#fff" stroke-width="2.5"><path d="M46 26 H33 V47 H53 V36"/><path d="M40 41 L41 37 L52 26 L55 29 L44 40 Z"/></g></svg>
  <div class="copy"><h3>Articles</h3><p>Request ad hoc payments for a product or service from anyone.</p></div>
</div>
<div class="feature" style="left:85px;top:728px">
  <svg><use href="#hex-blue"/><g fill="none" stroke="#fff" stroke-width="2.5"><path d="M46 26 H33 V47 H53 V36"/><path d="M40 41 L41 37 L52 26 L55 29 L44 40 Z"/></g></svg>
  <div class="copy"><h3>Events</h3><p>Create events and sell tickets from a consolidated interface.</p></div>
</div>

<div class="feature grey" style="left:422px;top:376px">
  <svg><use href="#hex-grey"/><g fill="#2a2a2a"><path d="M32 31 H52 L50 49 H34 Z"/></g><path d="M37 31 V28 Q42 21 47 28 V31" fill="none" stroke="#2a2a2a" stroke-width="2.5"/></svg>
  <div class="copy"><h3>Commerce</h3><p>Easily create an e-commerce site to sell your products</p></div>
</div>
<div class="feature grey" style="left:422px;top:464px">
  <svg><use href="#hex-grey"/><rect x="28" y="26" width="28" height="20" rx="2" fill="#2a2a2a"/><g fill="#fff"><rect x="31" y="31" width="10" height="2"/><rect x="31" y="35" width="10" height="2"/><rect x="31" y="39" width="10" height="2"/><circle cx="48" cy="33" r="3"/><rect x="44" y="37" width="8" height="5" rx="2"/></g></svg>
  <div class="copy"><h3>Memberships</h3><p>Manage Members with paid or free Membership Levels</p></div>
</div>
<div class="feature grey" style="left:422px;top:552px">
  <svg><use href="#hex-grey"/><g fill="#2a2a2a"><rect x="38" y="22" width="14" height="8" rx="1" transform="rotate(-35 45 26)"/><rect x="26" y="37" width="18" height="3" transform="rotate(-35 35 38)"/><rect x="44" y="44" width="14" height="5" rx="1"/></g></svg>
  <div class="copy"><h3>Auctions</h3><p>Manage donors, lots and bids.</p></div>
</div>
<div class="feature grey" style="left:422px;top:640px">
  <svg><use href="#hex-grey"/><rect x="36" y="22" width="18" height="26" rx="2" fill="#2a2a2a"/><g fill="#cfcfcf"><rect x="39" y="25" width="12" height="5"/><rect x="39" y="33" width="3" height="3"/><rect x="44" y="33" width="3" height="3"/><rect x="49" y="33" width="3" height="3"/><rect x="39" y="39" width="3" height="3"/><rect x="44" y="39" width="3" height="3"/><rect x="49" y="39" width="3" height="3"/></g><circle cx="35" cy="45" r="6" fill="#2a2a2a" stroke="#cfcfcf" stroke-width="1.5"/></svg>
  <div class="copy"><h3>Budgets</h3><p>Manage donors, lots and bids.</p></div>
</div>
<div class="feature grey" style="left:422px;top:728px">
  <svg><use href="#hex-grey"/><path d="M42 47 L30 35 Q27 31 30 27 Q35 23 42 30 Q49 23 54 27 Q57 31 54 35 Z" fill="#2a2a2a"/></svg>
  <div class="copy"><h3>Fundraisers</h3><p>Accept donations and allow donors to specify an earmark</p></div>
</div>

<section class="showcase" role="img" aria-label="Blue tinted photo of a laptop on a desk"></section>
<div class="device" style="left:68px;width:266px" role="img" aria-label="Laptop showing the members list in the dashboard"></div>
<div class="device" style="left:445px;width:265px" role="img" aria-label="Laptop showing an event page in a member space"></div>

<div class="showcase-caption" style="left:56px">
  <h2><span>Create</span> Content</h2>
  <p>Create a variety of free and paid content from a unified interface. Create a variety of free and paid content from a unified interface.</p>
</div>
<div class="showcase-caption" style="left:442px">
  <h2><span>Manage</span> Members</h2>
  <p>Create a variety of free and paid content from a unified interface. Create a variety of free and paid content from a unified interface.</p>
</div>

<section class="beta">
  <h2>Tallyroom.hive Is Currently In Beta.</h2>
  <div class="btn-site">CEATE SITE<svg width="13" height="8" viewBox="0 0 13 8"><path d="M0 4 H12 M8.5 0.8 L12 4 L8.5 7.2" fill="none" stroke="#222" stroke-width="1"/></svg></div>
</section>

<footer class="footer">Copyright © 2016 Tallyroom. All rights reserved.</footer>
</body>
</html>
```